Real Estate Entrepreneur needs a business card

I am a real estate entrepreneur, I buy houses for investment purposes, I act as a real estate agent representing buyers and sellers in residential home transactions, I am a contractor that does a wide range of home repairs and construction. I'd like a design that can stick with me through the years as my business grows and morphs to fit any niche I decide to pursue as markets change.

Target Market(s)

Anyone with interest that may be related to real estate.

Industry/Entity Type

Real Estate

Contact Information for Business Card

A card that stands out and doesn't put me in any one box. My business will evolve over time and I need a card that can stay relevant.

Colors

Designer to choose colors to be used in the design.

Requirements
Must have
• Character
Nice to have
• I'm open
Should not have
• Cliche houses and hammers

```html
<!DOCTYPE html>
<html lang="en">
<head>
<meta charset="utf-8">
<title>Drew Hale – Business Card</title>
<link rel="stylesheet" href="https://fonts.googleapis.com/css2?family=Ubuntu:wght@400;500;700&display=swap">
<style>
  :root {
    --page-bg-top: #f3f6f8;
    --page-bg-bottom: #e3e9ee;
    --card-bg: #2c2c2c;
    --accent: #f2a91f;
    --ink-light: #ffffff;
    --card-shadow: rgba(0, 0, 0, 0.45);
  }
  * { margin: 0; padding: 0; box-sizing: border-box; }
  html, body {
    width: 1200px;
    height: 2400px;
    overflow: hidden;
  }
  body {
    background: linear-gradient(180deg, var(--page-bg-top), var(--page-bg-bottom));
    font-family: "Ubuntu", sans-serif;
    position: relative;
  }
  .card {
    position: absolute;
    left: 64px;
    width: 1072px;
    height: 612px;
    background: var(--card-bg);
    overflow: hidden;
    box-shadow: 6px 10px 18px var(--card-shadow);
  }
  .card--back { top: 528px; }
  .card--front { top: 1260px; }

  /* Brand name placeholder in place of the monogram */
  .brand-mark {
    position: absolute;
    display: flex;
    align-items: center;
    gap: 16px;
    white-space: nowrap;
  }
  .brand-dot {
    width: 22px;
    height: 22px;
    border-radius: 50%;
    background: var(--accent);
    flex: none;
  }
  .brand-name {
    color: var(--accent);
    font-weight: 700;
    font-size: 46px;
    line-height: 1;
    letter-spacing: 1px;
  }
  .card--back .brand-mark { right: 44px; top: 60px; }
  .card--front .brand-mark { right: 44px; bottom: 64px; }

  .accent-bar {
    position: absolute;
    background: var(--accent);
  }
  .card--back .accent-bar { left: 0; bottom: 0; width: 450px; height: 22px; }
  .card--front .accent-bar { left: 0; top: 0; width: 408px; height: 16px; }

  /* Back: vertical identity */
  .identity-vertical {
    position: absolute;
    left: 70px;
    bottom: 56px;
    transform-origin: left bottom;
    transform: rotate(-90deg) translate(0, 100%);
    white-space: nowrap;
  }
  .person-name {
    color: var(--ink-light);
    font-weight: 700;
    font-size: 82px;
    line-height: 1;
    letter-spacing: 1px;
  }
  .person-role {
    color: var(--accent);
    font-weight: 400;
    font-size: 28px;
    line-height: 1.2;
    margin-top: 6px;
  }

  /* Front: horizontal identity */
  .identity-horizontal {
    position: absolute;
    left: 72px;
    top: 440px;
    white-space: nowrap;
  }
  .identity-horizontal .person-name { font-size: 88px; }

  .contact-list {
    position: absolute;
    left: 518px;
    top: 380px;
    list-style: none;
  }
  .contact-item {
    display: flex;
    align-items: center;
    height: 48px;
    color: var(--ink-light);
    font-size: 26px;
  }
  .contact-icon {
    width: 26px;
    height: 26px;
    margin-right: 20px;
    flex: none;
  }
</style>
</head>
<body>

  <section class="card card--back" aria-label="Card back">
    <div class="brand-mark">
      <span class="brand-dot"></span>
      <span class="brand-name">DREW HALE</span>
    </div>

    <div class="identity-vertical">
      <div class="person-name">DREW HALE</div>
      <div class="person-role">real estate entrepreneur</div>
    </div>

    <ul class="contact-list">
      <li class="contact-item">
        <svg class="contact-icon" viewBox="0 0 24 24" aria-hidden="true">
          <path fill="var(--accent)" d="M6.6 10.8a15.2 15.2 0 0 0 6.6 6.6l2.2-2.2c.3-.3.7-.4 1-.2 1.1.4 2.3.6 3.6.6.6 0 1 .4 1 1V20c0 .6-.4 1-1 1A17 17 0 0 1 3 4c0-.6.4-1 1-1h3.5c.6 0 1 .4 1 1 0 1.3.2 2.5.6 3.6.1.3 0 .7-.2 1z"/>
        </svg>
        +12 34 56 78 90 00
      </li>
      <li class="contact-item">
        <svg class="contact-icon" viewBox="0 0 24 24" aria-hidden="true">
          <rect x="2" y="5" width="20" height="14" rx="1" fill="var(--accent)"/>
          <path d="M2.5 5.8 12 13l9.5-7.2" fill="none" stroke="var(--card-bg)" stroke-width="1.8"/>
        </svg>
        your mail@goes here
      </li>
      <li class="contact-item">
        <svg class="contact-icon" viewBox="0 0 24 24" aria-hidden="true">
          <g fill="none" stroke="var(--accent)" stroke-width="2">
            <circle cx="12" cy="12" r="9.5"/>
            <ellipse cx="12" cy="12" rx="4.2" ry="9.5"/>
            <path d="M2.5 12h19M4 7h16M4 17h16"/>
          </g>
        </svg>
        www.yourwebsite.com
      </li>
      <li class="contact-item">
        <svg class="contact-icon" viewBox="0 0 24 24" aria-hidden="true">
          <rect x="11" y="3" width="2.4" height="19" fill="var(--accent)"/>
          <path d="M3 5h15l3 2.5L18 10H3z" fill="var(--accent)"/>
        </svg>
        123, your address will goes here
      </li>
    </ul>

    <div class="accent-bar"></div>
  </section>

  <section class="card card--front" aria-label="Card front">
    <div class="accent-bar"></div>

    <div class="brand-mark">
      <span class="brand-dot"></span>
      <span class="brand-name">DREW HALE</span>
    </div>

    <div class="identity-horizontal">
      <div class="person-name">DREW HALE</div>
      <div class="person-role">real estate entrepreneur</div>
    </div>
  </section>

</body>
</html>
```